2367 Halvorsen Avenue Medical Centre

We are looking for a design for new medical clinic.
We are accepting new patients at this new medical centre grand opening. Walk-ins are welcome.
Our cardiac and vascular surgical specialists are department heads at St Alder's Hospital, a leading teaching hospital in Toronto. These specialists will see cardiovascular consults are well as pre-surgical and post-surgical consultations and follow-ups.
Our lab is affiliated with several nuclear medicine clinics in the GTA.
Our Services Includes:
Family Practice
Cardiology Diagnostics
Cardiac & Vascular Surgical Consultation
Ultrasound & Vascular Testing
Open 6 days a week.
Ample Free Parking
Friendly Staffs

Target Market(s)

New Patients. Families of any age. Ethnic groups including Asians & Africans.

Industry/Entity Type

Medical

Font styles to use
Serif
Sans Serif
Decorative
Script
Other font styles liked:
• Arial calibri, verdana

Requirements
Must have
• Address:
• 2367 Halvorsen Avenue East
• Unit 225
• Scarborough, Ontario
• K7T 2P4
• Tel: (416) 555-0148
Nice to have
• Caring and inviting environment.
• Simple but classy.
• Standout colors.
Should not have
• Busy images. Aside from this, any ideas are welcome.

```html
<!DOCTYPE html>
<html lang="en">
<head>
<meta charset="utf-8">
<title>New Medical Clinic – Grand Opening</title>
<link href="https://fonts.googleapis.com/css2?family=Montserrat:wght@400;600;700;800&family=Open+Sans:wght@400;600&family=Great+Vibes&display=swap" rel="stylesheet">
<style>
  :root {
    --teal: #1fa68f;
    --teal-dark: #128170;
    --teal-light: #d8f0eb;
    --ink: #3b3b3b;
    --white: #ffffff;
    --paper: #f4f6f6;
  }
  * { box-sizing: border-box; margin: 0; padding: 0; }
  html, body { width: 831px; height: 1200px; overflow: hidden; background: var(--paper); }
  .flyer {
    position: relative; width: 831px; height: 1200px; overflow: hidden;
    background: linear-gradient(180deg, #ffffff 40%, #eef3f2 100%);
    font-family: "Open Sans", Arial, sans-serif; color: var(--ink);
  }
  .hero-photo {
    position: absolute; left: 0; top: 0; width: 831px; height: 450px;
    background: linear-gradient(120deg, #cfe3e6 0%, #eef4f5 45%, #f7f4f1 70%, #e9eef0 100%);
  }
  .hero-panel { position: absolute; left: 0; top: 0; width: 831px; height: 470px; }
  .brand-mark {
    position: absolute; left: 155px; top: 168px; width: 50px; height: 50px;
    border-radius: 50%; background: var(--white);
  }
  .headline {
    position: absolute; left: 30px; top: 228px; width: 300px;
    font-family: "Montserrat", Arial, sans-serif; font-weight: 800;
    color: var(--white); text-align: center; line-height: 1;
  }
  .headline .line-small { display: block; font-size: 33px; }
  .headline .line-big { display: block; font-size: 64px; margin-top: 2px; }
  .walk-in {
    position: absolute; left: 36px; top: 350px; width: 290px;
    border: 2px solid var(--white); padding: 6px 12px;
    font-family: "Montserrat", Arial, sans-serif; font-weight: 400;
    color: var(--white); font-size: 22px; line-height: 1.15; letter-spacing: .5px;
  }
  .open-badge { position: absolute; left: 450px; top: 245px; width: 330px; height: 215px; }
  .open-badge svg { position: absolute; left: 0; top: 0; }
  .open-badge .badge-label {
    position: absolute; left: 92px; top: 50px;
    font-family: "Montserrat", Arial, sans-serif; font-weight: 700; color: var(--teal-dark);
    font-size: 19px; line-height: 1.05;
  }
  .open-badge .badge-num {
    position: absolute; left: 188px; top: 30px;
    font-family: "Montserrat", Arial, sans-serif; font-weight: 800; color: var(--teal-dark); font-size: 76px; line-height: 1;
  }
  .open-badge .grand {
    position: absolute; left: 0; width: 330px; top: 126px; text-align: center;
    font-family: "Great Vibes", cursive; color: var(--white); font-size: 38px; line-height: 1.2;
  }
  .services-title {
    position: absolute; left: 340px; top: 505px; width: 150px; height: 34px;
    border: 2px solid var(--teal); border-radius: 17px; background: var(--white);
    text-align: center; line-height: 30px;
    font-family: "Montserrat", Arial, sans-serif; font-weight: 700; color: var(--teal-dark); font-size: 17px;
  }
  .services-rule { position: absolute; left: 110px; right: 110px; top: 521px; height: 2px; background: var(--teal-light); }
  .service-list { position: absolute; left: 110px; top: 555px; width: 611px; display: flex; gap: 17px; list-style: none; }
  .service {
    width: 140px; height: 140px; background: var(--teal); color: var(--white);
    text-align: center; padding-top: 12px;
    font-family: "Montserrat", Arial, sans-serif; font-weight: 600; font-size: 13px; line-height: 1.2;
    box-shadow: 0 3px 6px rgba(0,0,0,.18);
  }
  .service .service-name { height: 48px; display: flex; align-items: center; justify-content: center; padding: 0 8px; }
  .service .service-icon { width: 58px; height: 58px; margin: 8px auto 0; border-radius: 50%; background: rgba(255,255,255,.85); }
  .about {
    position: absolute; left: 105px; top: 730px; width: 621px; height: 172px;
    border: 2px solid var(--teal); background: var(--white); border-radius: 4px;
    text-align: center; padding: 14px 30px 0;
  }
  .about .about-mark { width: 34px; height: 34px; border-radius: 50%; background: var(--teal); margin: 0 auto 10px; }
  .about p { font-size: 13px; line-height: 1.45; color: var(--ink); }
  .perks { display: flex; justify-content: center; gap: 120px; margin-top: 12px; font-size: 13px; font-weight: 600; }
  .perks li { list-style: none; display: flex; align-items: center; gap: 6px; }
  .pin { position: absolute; left: 403px; top: 912px; }
  .address {
    position: absolute; left: 0; width: 831px; top: 948px; text-align: center;
    font-family: "Montserrat", Arial, sans-serif; font-weight: 700; font-style: normal; color: var(--teal-dark);
    font-size: 34px; line-height: 1.2;
  }
  .booking {
    position: absolute; left: 0; bottom: 0; width: 831px; height: 92px; background: var(--teal);
    display: flex; align-items: center; justify-content: center; gap: 14px; color: var(--white);
    font-family: "Montserrat", Arial, sans-serif;
  }
  .booking .lead { font-size: 17px; font-weight: 600; }
  .booking .phone { font-size: 38px; font-weight: 800; }
</style>
</head>
<body>
<main class="flyer">
  <div class="hero-photo" role="img" aria-label="Photo of a smiling female doctor with stethoscope in a bright clinic, a colleague with a patient in the background"></div>

  <svg class="hero-panel" viewBox="0 0 831 470" aria-hidden="true">
    <path d="M0 150 L360 150 L360 450 L0 470 Z" fill="#1fa68f" opacity=".92"/>
    <path d="M360 150 L360 450 L395 300 Z" fill="#128170"/>
  </svg>

  <div class="brand-mark"></div>
  <h1 class="headline"><span class="line-small">NEW MEDICAL</span><span class="line-big">CLINIC</span></h1>
  <div class="walk-in">ACCEPTING<br>WALK-IN PATIENTS</div>

  <div class="open-badge">
    <svg width="330" height="215" viewBox="0 0 330 215" aria-hidden="true">
      <circle cx="165" cy="98" r="92" fill="#ffffff" stroke="#1fa68f" stroke-width="6"/>
      <path d="M10 128 L320 128 L300 156 L320 186 L10 186 L30 156 Z" fill="#128170"/>
      <path d="M30 120 Q165 158 300 120 L300 178 Q165 213 30 178 Z" fill="#1fa68f"/>
    </svg>
    <div class="badge-label">OPEN<br>DAYS<br>A WEEK</div>
    <div class="badge-num">6</div>
    <div class="grand">Grand Opening</div>
  </div>

  <div class="services-rule"></div>
  <h2 class="services-title">SERVICES</h2>
  <ul class="service-list">
    <li class="service"><div class="service-name">Family Practice</div><div class="service-icon" role="img" aria-label="Stethoscope icon"></div></li>
    <li class="service"><div class="service-name">Cardiology Diagnostics</div><div class="service-icon" role="img" aria-label="Heart illustration icon"></div></li>
    <li class="service"><div class="service-name">Cardiac &amp; Vascular Surgical Consultation</div><div class="service-icon" role="img" aria-label="Doctor consultation icon"></div></li>
    <li class="service"><div class="service-name">Ultrasound &amp; Vascular Testing</div><div class="service-icon" role="img" aria-label="Ultrasound scanner icon"></div></li>
  </ul>

  <section class="about">
    <div class="about-mark"></div>
    <p>Our cardiac and vascular surgical specialists are department heads at St Alder's Hospital, a leading teaching hospital in Toronto. These specialists will see cardiovascular consults are well as pre-surgical and post-surgical consultations and follow-ups.<br>Our lab is affiliated with several nuclear medicine clinics in the GTA.</p>
    <ul class="perks">
      <li><svg width="14" height="14" viewBox="0 0 14 14"><path d="M1 7 L5 11 L13 2" fill="none" stroke="#1fa68f" stroke-width="2.5"/></svg>Ample Free Parking</li>
      <li><svg width="14" height="14" viewBox="0 0 14 14"><path d="M1 7 L5 11 L13 2" fill="none" stroke="#1fa68f" stroke-width="2.5"/></svg>Friendly Staffs</li>
    </ul>
  </section>

  <svg class="pin" width="24" height="30" viewBox="0 0 24 30" aria-hidden="true">
    <path d="M12 0 C5 0 0 5 0 12 C0 20 12 30 12 30 C12 30 24 20 24 12 C24 5 19 0 12 0 Z" fill="#1fa68f"/>
    <circle cx="12" cy="12" r="4.5" fill="#ffffff"/>
  </svg>
  <address class="address">2367 Halvorsen Avenue East Unit 225<br>Scarborough, Ontario K7T 2P4</address>

  <footer class="booking">
    <span class="lead">TO BOOK APPOINTMENT, PLEASE</span>
    <span class="phone">CALL (416) 555-0148</span>
  </footer>
</main>
</body>
</html>
```